Harlowe plumbing business cards

Want a functional designed for my business cards using my logo

Company Name- Harlowe Plumbing, Heating & Water Systems
Name- Marcus Harlowe
Title- Vice President
Cell- 555-318-7426
Email- Harloweplumbing@mailbrook.net
Business address-
PO Box 37
Fenwick Mill, MD 21999

Industry/Entity Type

Plumbing

```html
<!DOCTYPE html>
<html lang="en">
<head>
<meta charset="utf-8">
<title>Harlowe Plumbing business cards</title>
<link rel="stylesheet" href="https://fonts.googleapis.com/css2?family=Open+Sans:wght@400;600;700&display=swap">
<style>
  :root {
    --backdrop: #3b3c3e;
    --card-dark: #2c2d30;
    --card-blue: #4f82c3;
    --wave-blue: #1f6fc9;
    --wave-white: #f4f6f8;
    --text-white: #ffffff;
    --text-dark: #2e3136;
    --text-muted: #34465e;
    --accent-blue: #2a7ad6;
  }
  html, body {
    margin: 0;
    width: 1200px;
    height: 717px;
    overflow: hidden;
    background: var(--backdrop);
    font-family: "Open Sans", Arial, sans-serif;
  }
  .sheet { position: relative; width: 1200px; height: 717px; }
  .card {
    position: absolute;
    top: 208px;
    width: 525px;
    height: 300px;
    overflow: hidden;
    border-radius: 3px;
    box-shadow: 0 10px 28px rgba(0,0,0,0.45);
  }
  .card--front { left: 50px; background: var(--card-dark); }
  .card--back { left: 625px; background: var(--card-blue); }
  .card__wave { position: absolute; left: 0; top: 0; width: 525px; height: 300px; }
  .brand { position: absolute; line-height: 1.05; font-weight: 400; white-space: nowrap; }
  .brand__name { display: block; font-size: 30px; }
  .brand__tagline { display: block; font-size: 17px; margin-top: 2px; }
  .brand__mark {
    display: inline-block;
    width: 10px; height: 10px;
    border-radius: 50%;
    margin-right: 8px;
    vertical-align: middle;
  }
  .phone-main { position: absolute; letter-spacing: 0.5px; white-space: nowrap; }

  .card--front .brand { left: 150px; top: 52px; color: var(--text-white); }
  .card--front .brand__mark { background: var(--accent-blue); }
  .card--front .phone-main { left: 150px; top: 124px; font-size: 25px; color: var(--accent-blue); }

  .person { position: absolute; left: 40px; top: 30px; }
  .person__name { margin: 0; font-size: 18px; font-weight: 700; color: var(--text-white); }
  .person__title { margin: 2px 0 0; font-size: 12.5px; color: var(--text-muted); }
  .contact-list {
    position: absolute;
    left: 40px; top: 96px;
    margin: 0; padding: 0;
    list-style: none;
    font-size: 12.5px;
    color: var(--text-white);
    line-height: 1.5;
  }
  .contact-list li { display: flex; align-items: flex-start; gap: 7px; }
  .contact-list .icon {
    flex: none;
    width: 12px; height: 12px;
    margin-top: 3px;
    background: var(--text-dark);
    border-radius: 2px;
  }

  .card--back .brand { right: 26px; top: 140px; color: var(--text-dark); }
  .card--back .brand__mark { background: var(--text-dark); }
  .card--back .phone-main { right: 60px; top: 198px; font-size: 27px; color: var(--text-dark); }
</style>
</head>
<body>
<main class="sheet">

  <section class="card card--front" aria-label="Business card front">
    <svg class="card__wave" viewBox="0 0 525 300" aria-hidden="true">
      <path d="M0,165 C190,160 330,255 525,262 V300 H0 Z" fill="var(--wave-blue)"/>
      <path d="M0,183 C190,182 330,272 525,278 V300 H0 Z" fill="var(--wave-white)"/>
      <path d="M0,190 C190,191 330,281 525,286 V300 H0 Z" fill="var(--wave-blue)"/>
    </svg>
    <div class="brand">
      <span class="brand__name"><span class="brand__mark"></span>Harlowe Plumbing</span>
      <span class="brand__tagline">Heating &amp; Water Systems</span>
    </div>
    <div class="phone-main">555.204.6183</div>
  </section>

  <section class="card card--back" aria-label="Business card back">
    <svg class="card__wave" viewBox="0 0 525 300" aria-hidden="true">
      <path d="M0,200 C170,200 300,268 525,272 V300 H0 Z" fill="var(--wave-blue)"/>
      <path d="M0,214 C180,216 310,280 525,282 V300 H0 Z" fill="var(--wave-white)"/>
      <path d="M0,221 C180,224 310,288 525,290 V300 H0 Z" fill="var(--wave-blue)"/>
    </svg>

    <div class="person">
      <h1 class="person__name">Marcus Harlowe</h1>
      <p class="person__title">Vice President</p>
    </div>

    <ul class="contact-list">
      <li>
        <svg class="icon" viewBox="0 0 12 12" aria-hidden="true"><path d="M3 2.5h2l.7 2-1.2.8a5 5 0 0 0 2.2 2.2l.8-1.2 2 .7v2a1 1 0 0 1-1 1A7 7 0 0 1 2 3.5a1 1 0 0 1 1-1z" fill="#fff"/></svg>
        <span>555-318-7426</span>
      </li>
      <li>
        <svg class="icon" viewBox="0 0 12 12" aria-hidden="true"><rect x="2.5" y="3.5" width="7" height="5" fill="none" stroke="#fff" stroke-width="1"/><path d="M2.5 3.5 6 6.5 9.5 3.5" fill="none" stroke="#fff" stroke-width="1"/></svg>
        <span>Harloweplumbing@mailbrook.net</span>
      </li>
      <li>
        <svg class="icon" viewBox="0 0 12 12" aria-hidden="true"><path d="M6 2a2.5 2.5 0 0 1 2.5 2.5C8.5 6.5 6 10 6 10S3.5 6.5 3.5 4.5A2.5 2.5 0 0 1 6 2z" fill="#fff"/><circle cx="6" cy="4.5" r="0.9" fill="var(--text-dark)"/></svg>
        <span>PO Box 37<br>Fenwick Mill, MD 21999</span>
      </li>
    </ul>

    <div class="brand">
      <span class="brand__name"><span class="brand__mark"></span>Harlowe Plumbing</span>
      <span class="brand__tagline">Heating &amp; Water Systems</span>
    </div>
    <div class="phone-main">555.204.6183</div>
  </section>

</main>
</body>
</html>
```